Marketing Collateral Project
Cedarwick Falls Business Association
Marketing Collateral Project - Business Opportunities
Business Opportunities
Locally based small and large businesses including professional services, manufacturing, retail and medical. The brochure should look professional and help the organization establish credibility.
Four panel brochure: Panels 1-3 should include areas for some of the following content: Our Mission, About Us, Top 10 Reasons to Join, Events, Committees, Membership Level Outline/Benefits, our contact info Panel 4: This panel should be able to be detached and mailed without an envelope. So one side will include a form collecting the information: Name, Title, Company, Address(Street, City, State, Zip) phone: business & alternate, fax, email; Membership Type (select one) Bronze - $100 Silver - $150 Gold - $250 Platinum - $350

```html
<!DOCTYPE html>
<html lang="en">
<head>
<meta charset="utf-8">
<title>Cedarwick Falls Business Association – Brochure</title>
<link href="https://fonts.googleapis.com/css2?family=Arimo:ital,wght@0,400;0,700;1,700&display=swap" rel="stylesheet">
<style>
:root{
  --navy:#1a2868;
  --blue:#2c4ea3;
  --gold:#f4b71c;
  --ink:#333a4a;
  --bg:#e9e9ec;
  --white:#ffffff;
  --rule:#9aa2b3;
}
*{box-sizing:border-box;margin:0;padding:0}
html,body{width:1200px;height:988px;overflow:hidden;background:var(--bg);font-family:"Arimo",Arial,sans-serif;color:var(--ink)}
.sheet{position:absolute;top:144px;width:540px;height:700px;background:var(--white);box-shadow:0 4px 14px rgba(0,0,0,.18);overflow:hidden}
.front{left:40px}
.back{left:620px}

/* brand */
.brand{display:flex;align-items:center;gap:10px}
.brand-square{width:34px;height:34px;background:var(--blue);flex:none}
.brand-name{font-weight:700;color:var(--navy);text-transform:uppercase;line-height:1.1}
.front .brand{position:absolute;left:40px;top:30px}
.front .brand-square{width:56px;height:56px}
.front .brand-name{font-size:19px;width:300px}
.tagline{position:absolute;left:40px;top:98px;width:460px;border-top:2px solid var(--gold);color:var(--navy);font-size:11px;font-weight:700;letter-spacing:2px;padding:6px 0 0;text-transform:uppercase}

.front-photos{position:absolute;left:0;top:130px;width:540px;height:300px;background:linear-gradient(180deg,#8fb2dc 0%,#c9d6e3 45%,#8a8f95 100%)}
.front-band{position:absolute;left:0;top:400px;width:540px;height:300px}
.slogans{position:absolute;right:34px;top:478px;text-align:right;color:var(--white);font-style:italic;font-weight:700;font-size:27px;line-height:1.18}
.connect{position:absolute;right:34px;top:588px;width:300px;text-align:right;color:var(--gold);font-size:14px;line-height:1.35}
.front-web{position:absolute;left:26px;bottom:18px;color:var(--white);font-size:11px}

/* back page */
.back-head{position:absolute;left:18px;top:16px;width:220px}
.back-head .brand-name{font-size:11px}
.back-head .tagline-sm{margin-top:5px;border-top:1.5px solid var(--gold);color:var(--navy);font-size:6.5px;font-weight:700;letter-spacing:1px;padding-top:3px;text-transform:uppercase}
.back-head .contact{margin-top:5px;font-size:8px;line-height:1.4;color:var(--ink)}
.back-photo{position:absolute;left:18px;top:110px;width:220px;height:90px;background:linear-gradient(135deg,#a9bcd4,#6e7e92)}

.left-col{position:absolute;left:18px;top:212px;width:220px}
.right-col{position:absolute;left:256px;top:24px;width:266px}
h2{font-size:16px;font-weight:700;color:var(--navy);border-bottom:2px solid var(--gold);padding-bottom:2px;margin-bottom:6px}
.right-col h2 + p{margin-top:0}
.right-col .section{margin-top:10px}
h3{font-size:10px;font-weight:700;color:var(--blue);margin:8px 0 3px}
p,li{font-size:8.5px;line-height:1.45}
ul{padding-left:11px}
.join-bar{background:var(--blue);color:var(--white);font-size:8.5px;padding:5px 7px;margin:5px 0 8px;line-height:1.35}
.join-bar b{display:block;color:var(--gold);font-size:9.5px}
.form-row{display:flex;align-items:flex-end;gap:5px;height:15px;font-size:8px}
.form-row span{white-space:nowrap}
.form-row i{flex:1;border-bottom:1px solid var(--rule);height:1px}
.levels{margin-top:8px;font-size:8.5px;font-weight:700;color:var(--navy)}
.level-grid{display:grid;grid-template-columns:1fr 1fr;gap:4px 10px;margin-top:5px;font-weight:400;color:var(--ink)}
.level-grid span::before{content:"";display:inline-block;width:7px;height:7px;border:1px solid var(--navy);margin-right:5px;vertical-align:-1px}
.payment{margin-top:10px;text-align:center;font-size:9.5px;font-weight:700;color:var(--navy);line-height:1.3}
.back-foot{position:absolute;left:0;bottom:0;width:540px;height:22px;background:var(--navy);color:var(--white);font-size:9px;font-weight:700;display:flex;align-items:center;justify-content:flex-end;padding-right:18px;border-top:3px solid var(--gold)}
</style>
</head>
<body>

<section class="sheet front">
  <div class="brand">
    <span class="brand-square"></span>
    <span class="brand-name">Cedarwick Falls Business Association</span>
  </div>
  <div class="tagline">Growing Business. Connecting Neighbors</div>
  <div class="front-photos" role="img" aria-label="Collage of local office buildings and members at a community event"></div>
  <svg class="front-band" viewBox="0 0 540 300" width="540" height="300" aria-hidden="true">
    <path d="M0 60 Q270 -10 540 40 L540 300 L0 300 Z" fill="var(--navy)"/>
    <path d="M0 60 Q270 -10 540 40 L540 56 Q270 8 0 78 Z" fill="var(--gold)"/>
    <path d="M0 78 Q270 8 540 56 L540 66 Q270 22 0 92 Z" fill="var(--blue)"/>
  </svg>
  <div class="slogans">It's about people.<br>It's about ideas.<br>It's about influence.</div>
  <div class="connect">The power of connection: your business thrives on it. Connect with success at the CFBA!</div>
  <div class="front-web">www.cedarwickfallsbusiness.com</div>
</section>

<section class="sheet back">
  <div class="back-head">
    <div class="brand">
      <span class="brand-square"></span>
      <span class="brand-name">Cedarwick Falls Business Association</span>
    </div>
    <div class="tagline-sm">Growing Business. Connecting Neighbors</div>
    <div class="contact">4120 Millrace Parkway, Cedarwick Falls, MN 55490<br>Phone: 555-014-2286</div>
  </div>
  <div class="back-photo" role="img" aria-label="Photo of members meeting at an association event"></div>

  <div class="left-col">
    <h2>Membership</h2>
    <p>Membership is open to any business or organization that shares our goals.</p>
    <div class="join-bar"><b>To Become a Member:</b>Complete the form below and mail to the CFBA or apply online.</div>
    <div class="form-row"><span>Type of Business:</span><i></i></div>
    <div class="form-row"><span>Company Name:</span><i></i></div>
    <div class="form-row"><span>Number of Employees:</span><i></i></div>
    <div class="form-row"><span>Job Title:</span><i></i></div>
    <div class="form-row"><span>First Name:</span><i></i></div>
    <div class="form-row"><span>Last Name:</span><i></i></div>
    <div class="form-row"><span>Address:</span><i></i></div>
    <div class="form-row"><span>City/State/Zip:</span><i></i></div>
    <div class="form-row"><span>Company Phone:</span><i></i></div>
    <div class="form-row"><span>Fax:</span><i></i></div>
    <div class="form-row"><span>Cell Phone:</span><i></i></div>
    <div class="form-row"><span>Email:</span><i></i></div>
    <div class="form-row"><span>Website:</span><i></i></div>
    <div class="levels">Membership Type:
      <div class="level-grid">
        <span>Bronze – $100</span><span>Silver – $150</span>
        <span>Gold – $250</span><span>Platinum – $350</span>
      </div>
    </div>
    <div class="payment">Please make payment online<br>or by check to the CFBA</div>
  </div>

  <div class="right-col">
    <h2>About the CFBA</h2>
    <p>The Cedarwick Falls Business Association is a voluntary organization of businesses, community organizations and individuals who work together to promote commerce and build community across the city and the wider region.</p>
    <p>We offer members networking, advocacy and visibility, and we partner with local government to keep our business district strong and welcoming.</p>
    <div class="section">
      <h2>Our Mission</h2>
      <p>To strengthen the local economy by connecting businesses, sharing resources and representing member interests in every civic decision that shapes our community.</p>
      <h3>Top Reasons to Join</h3>
      <ul>
        <li>Meet other business leaders at monthly events</li>
        <li>Promote your company to local customers</li>
        <li>Stay informed on city plans and policies</li>
        <li>Gain visibility through our member directory</li>
        <li>Join committees that shape the district</li>
      </ul>
    </div>
    <div class="section">
      <h2>Community</h2>
      <p>Our members sponsor school programs, park clean-ups and holiday drives, giving back to the neighborhoods where we live and work every day.</p>
    </div>
    <div class="section">
      <h2>Events</h2>
      <p>Join us for breakfast forums, business expos and our annual awards dinner. Visit our website for the full calendar.</p>
    </div>
  </div>

  <div class="back-foot">www.cedarwickfallsbusiness.com</div>
</section>

</body>
</html>
```